Velto an Organic Supplement Brand

A product label for a Supplement Brand. Company is called "Velto" and the tagline is "Healing Takes A Village". Their will be multiple products such as capsules, liquids, powders, etc. Lets focus on Vitamin C capsules, but if you want to play around with color pallets and or multiple supplements that would be great. Want it to be a simple, clean and sophisticated design that looks fresh and stands out. This product has high quality organic ingredients. Attached is label specifications as well as an image for stock language for left and right side of label for reference and some sample products. Parts can be omitted, added or mixed and matched as needed.
Target Market(s)
Moms
Industry/Entity Type
Health and Wellness
Look and feel

```html
<!DOCTYPE html>
<html lang="en">
<head>
<meta charset="UTF-8">
<title>Velto Vitamin C Label</title>
<link href="https://fonts.googleapis.com/css2?family=Montserrat:wght@400;500;600;700;900&display=swap" rel="stylesheet">
<style>
  :root {
    --canvas: #e7e7e7;
    --label: #ffffff;
    --ink: #231f1c;
    --ink-soft: #4a4643;
    --amber: #f0b52c;
    --rule: #f3d77c;
  }
  html, body {
    margin: 0;
    padding: 0;
    width: 1200px;
    height: 1200px;
    overflow: hidden;
    background: var(--canvas);
    font-family: "Montserrat", sans-serif;
  }
  .label {
    position: absolute;
    left: 110px;
    top: 80px;
    width: 980px;
    height: 1040px;
    background: var(--label);
    overflow: hidden;
  }
  .label__rule {
    position: absolute;
    left: 0; right: 0; top: 0;
    height: 2px;
    background: var(--rule);
  }
  .label__wave {
    position: absolute;
    left: 0; top: 0;
    width: 980px;
    height: 1040px;
  }
  .product-name,
  .category {
    position: absolute;
    writing-mode: vertical-rl;
    transform: rotate(180deg);
    margin: 0;
    white-space: nowrap;
    line-height: 1;
  }
  .product-name {
    left: 190px;
    top: 97px;
    height: 889px;
    font-size: 152px;
    font-weight: 900;
    letter-spacing: 2px;
    color: var(--ink);
    z-index: 2;
  }
  .category {
    left: 160px;
    top: 128px;
    height: 410px;
    font-size: 30px;
    font-weight: 500;
    letter-spacing: 3px;
    color: var(--ink-soft);
  }
  .brand {
    position: absolute;
    left: 567px;
    top: 58px;
    width: 330px;
    text-align: center;
  }
  .brand__name {
    margin: 0;
    font-size: 56px;
    font-weight: 500;
    letter-spacing: 11px;
    color: var(--ink-soft);
    line-height: 1.1;
  }
  .citrus {
    position: absolute;
    left: 400px;
    top: 198px;
    width: 376px;
    height: 376px;
  }
  .count {
    position: absolute;
    left: 700px;
    top: 775px;
    display: flex;
    align-items: flex-start;
    gap: 8px;
    color: var(--ink);
  }
  .count__icon { width: 40px; height: 88px; }
  .count__text { display: flex; flex-direction: column; }
  .count__number {
    font-size: 60px;
    font-weight: 700;
    line-height: 0.95;
  }
  .count__unit {
    font-size: 16px;
    font-weight: 500;
    letter-spacing: 1px;
  }
  .count__dose {
    position: absolute;
    left: 752px;
    top: 873px;
    font-size: 22px;
    font-weight: 500;
    letter-spacing: 1px;
    color: var(--ink);
  }
  .format {
    position: absolute;
    left: 0;
    right: 0;
    top: 932px;
    height: 68px;
    background: var(--amber);
  }
  .format__text {
    position: absolute;
    left: 380px;
    top: 16px;
    margin: 0;
    font-size: 30px;
    font-weight: 600;
    letter-spacing: 4.5px;
    color: var(--ink);
    line-height: 1.1;
  }
</style>
</head>
<body>
  <div class="label">
    <div class="label__rule"></div>

    <svg class="label__wave" viewBox="0 0 980 1040" aria-hidden="true">
      <defs>
        <linearGradient id="sunband" x1="0" y1="0" x2="0" y2="1">
          <stop offset="0" stop-color="#f7c940"/>
          <stop offset="1" stop-color="#eab026"/>
        </linearGradient>
      </defs>
      <path d="M0 662 C100 650 220 720 320 722 C420 724 480 655 560 652 C700 648 850 690 980 708 L980 1040 L0 1040 Z" fill="url(#sunband)"/>
    </svg>

    <h2 class="category">DIETARY SUPPLEMENT</h2>
    <h1 class="product-name">VITAMIN C</h1>

    <div class="brand">
      <p class="brand__name">VELTO</p>
    </div>

    <svg class="citrus" viewBox="0 0 376 376" role="img" aria-label="Illustration of a sliced citrus fruit">
      <circle cx="188" cy="188" r="186" fill="#f5c23c"/>
    </svg>

    <div class="count">
      <svg class="count__icon" viewBox="0 0 42 90" aria-hidden="true">
        <rect x="3" y="3" width="36" height="84" rx="18" fill="none" stroke="#231f1c" stroke-width="5"/>
        <path d="M3 45 V21 A18 18 0 0 1 39 21 V45 Z" fill="#231f1c"/>
      </svg>
      <div class="count__text">
        <span class="count__number">180</span>
        <span class="count__unit">CAPSULES</span>
      </div>
    </div>
    <div class="count__dose">500 MG</div>

    <div class="format">
      <p class="format__text">VEGETARIAN CAPSULES</p>
    </div>
  </div>
</body>
</html>
```